Pellora Networks web design

Pellora is an Internet Service Provider bringing high-speed service to homes and businesses. Our principal market target is rural areas of West Michigan, but we intend to expand rapidly. We need a website to market our services, facilitate online ordering, customer support and communicate with our customers.

I will upload a draft outline of the content we hope to include in the website.

We compete directly with Bramwell Communications, Quendar, Lumitek and Hollister communications to bring Internet service to homes and businesses in our coverage area.

Our primary values include:

1. Unlike our competitors, we do not require long term contractors or service bundles; There are no termination fees, for example. All services are sold on a recurring 1-month agreement term.
2. Unlike other wireless (mobile) providers, we do not limit downloads or uploads with bit/byte buckets
3. We provide service to areas ignored by the larger carriers - Rural areas in Michigan that lack options for broadband are prime targets for Pellora to cover.
4. Unlike other wireless ISP's, we utilize licensed FCC spectrum. We do not use unlicensed/free frequencies, providing us an advantage for reliability and stability.

So many wonderful designs, thank you very much for all your hard work. We are evaluating all our favorite designs and plan to make a selection in the next 2 days. I will be in touch with you to request revisions if necessary or further refinements.  Thank you again for your efforts on this project.

Target Market(s)

Our target market is home Internet users. however, that does not mean that our users are "high tech" oriented - they are just normal mom's and pop's who buy Internet for home use. The site should be easy to navigate and communicate our message of speed, value, reliability and facilitate simple product ordering.

Industry/Entity Type

Internet

Requirements
Must have
• Our phone number should be prominently displayed 1-844-7RU-NLOK
• Our logo is uploaded in the attachments.
• Design for desktop and mobile devices.
Nice to have
• The most modern of web design trends. Such as a design that facilitates parallax scrolling effects rather than lots of individual pages.
• Stock artwork communicating our values of speed and reliability.

```html
<!DOCTYPE html>
<html lang="en">
<head>
<meta charset="utf-8">
<title>Pellora Networks – Mobile Screens</title>
<link rel="stylesheet" href="https://fonts.googleapis.com/css2?family=Roboto:wght@100;300;400;500;700&family=PT+Serif&display=swap">
<style>
  :root {
    --orange: #f57b10;
    --orange-deep: #e0600a;
    --sky-dark: #b8420c;
    --sky-light: #f59a3a;
    --ink: #5f5f5f;
    --ink-soft: #7a7a7a;
    --grey-bar: #7b7b7b;
    --sub-bg: #efefef;
    --page: #ffffff;
    --stage: #f4f4f4;
    --dark-arrow: #3a3a3a;
    --tap: rgba(70, 150, 230, 0.55);
  }
  * { box-sizing: border-box; margin: 0; padding: 0; }
  html, body { width: 1200px; height: 860px; overflow: hidden; background: var(--stage); }
  body { font-family: "Roboto", Arial, sans-serif; color: var(--ink); }

  .stage { position: absolute; left: 0; top: 0; width: 960px; height: 688px; transform: scale(1.25); transform-origin: 0 0; }

  .screen { position: absolute; top: 24px; width: 265px; background: var(--page); overflow: hidden; box-shadow: 0 0 0 1px #d8d8d8; }
  .screen--home { left: 40px; height: 640px; }
  .screen--menu { left: 348px; height: 396px; }
  .screen--search { left: 656px; height: 396px; }

  .app-header { position: absolute; left: 0; top: 0; width: 265px; height: 62px; background: var(--page); }
  .icon-burger, .icon-search { position: absolute; }
  .brand { position: absolute; left: 50px; top: 21px; width: 165px; text-align: center; font-weight: 700; font-size: 14px; letter-spacing: .5px; color: var(--orange); line-height: 20px; text-transform: uppercase; white-space: nowrap; }

  .tagline-strip { position: absolute; left: 0; top: 62px; width: 265px; height: 16px; background: var(--orange); color: #fff; font-size: 9.5px; line-height: 16px; text-align: center; letter-spacing: .2px; white-space: nowrap; }

  .hero { position: absolute; left: 0; top: 78px; width: 265px; height: 117px; background: linear-gradient(160deg, var(--sky-light) 0%, var(--orange-deep) 45%, var(--sky-dark) 100%); }
  .hero__big { position: absolute; left: 12px; top: 6px; font-weight: 100; font-size: 54px; color: #fff; line-height: 60px; }
  .hero__words { position: absolute; left: 157px; top: 10px; font-weight: 300; font-size: 24px; line-height: 22px; color: #fff; }

  .tabs { position: absolute; left: 10px; top: 158px; width: 247px; height: 37px; }
  .tab { position: absolute; top: 0; height: 37px; font-size: 10.5px; line-height: 12px; text-align: center; padding-top: 6px; color: #fff; background: rgba(255,255,255,.28); border-radius: 3px 3px 0 0; }
  .tab--active { background: var(--page); color: #333; }

  .section-title { position: absolute; left: 34px; top: 225px; font-weight: 700; font-size: 15px; color: var(--ink); }
  .soft-shadow { position: absolute; left: 30px; width: 205px; height: 12px; border-radius: 50%; background: radial-gradient(ellipse at center, rgba(0,0,0,.22), rgba(0,0,0,0) 70%); }

  .plan { position: absolute; left: 0; top: 283px; width: 265px; text-align: center; }
  .plan__name { font-weight: 700; font-size: 14px; color: var(--ink); line-height: 18px; }
  .plan__spec { font-size: 12px; line-height: 17px; color: var(--ink-soft); }
  .price { position: absolute; left: 0; top: 338px; width: 265px; text-align: center; color: var(--orange); font-weight: 100; }
  .price__cur { font-size: 20px; vertical-align: top; font-weight: 300; position: relative; top: 4px; }
  .price__main { font-size: 58px; line-height: 56px; }
  .price__cents { font-size: 18px; vertical-align: top; font-weight: 300; position: relative; top: 4px; }

  .slider-arrow { position: absolute; top: 349px; width: 33px; height: 33px; border-radius: 50%; }
  .slider-arrow--prev { left: 3px; background: #9c9c9c; }
  .slider-arrow--next { left: 226px; background: var(--dark-arrow); }

  .install-fee { position: absolute; left: 0; top: 411px; width: 265px; text-align: center; font-size: 15px; color: var(--ink); font-weight: 300; }
  .btn-buy { position: absolute; left: 57px; top: 446px; width: 142px; height: 50px; background: var(--orange); color: #fff; font-size: 15px; font-weight: 300; line-height: 50px; text-align: center; }

  .dots { position: absolute; left: 95px; top: 528px; }
  .dot { display: inline-block; width: 16px; height: 16px; border-radius: 50%; background: #a8a8a8; margin-right: 7px; }
  .dot--on { background: var(--orange); }

  .hotline { position: absolute; left: 8px; top: 602px; width: 260px; color: var(--orange); font-weight: 100; font-size: 27px; line-height: 32px; white-space: nowrap; }
  .hotline svg { vertical-align: -2px; margin-right: 4px; }

  .drawer { position: absolute; left: 0; top: 0; width: 206px; height: 396px; background: var(--page); box-shadow: 3px 0 5px rgba(0,0,0,.18); z-index: 2; }
  .drawer__item { position: absolute; left: 0; width: 206px; height: 36px; line-height: 36px; padding-left: 17px; font-size: 12.5px; color: var(--orange); }
  .drawer__item--open { background: var(--grey-bar); color: #fff; }
  .drawer__item--sub { background: var(--sub-bg); padding-left: 34px; border-bottom: 1px solid #e6e6e6; }
  .drawer__item--current { background: var(--orange); color: #fff; padding-left: 34px; }
  .drawer__toggle { position: absolute; right: 0; top: 0; width: 36px; height: 36px; border-left: 1px solid #929292; }
  .tap-mark { position: absolute; left: 36px; top: 250px; width: 43px; height: 43px; border-radius: 50%; background: var(--tap); border: 1.5px solid #3d8ede; }

  .peek { position: absolute; top: 0; height: 396px; background: var(--page); overflow: hidden; }

  .search-panel { position: absolute; left: 59px; top: 0; width: 206px; height: 396px; background: var(--page); box-shadow: -3px 0 5px rgba(0,0,0,.18); }
  .search-panel__bar { height: 67px; background: var(--orange); padding: 14px 14px 0 14px; }
  .search-field { position: relative; height: 36px; background: #fff; border-radius: 3px; }
  .search-field__input { position: absolute; left: 0; top: 0; width: 140px; height: 36px; padding-left: 8px; line-height: 36px; font-family: "PT Serif", Georgia, serif; font-size: 12.5px; color: #9a9a9a; border-right: 1px solid #e2e2e2; }
  .search-field__btn { position: absolute; right: 8px; top: 8px; }
</style>
</head>
<body>
<main class="stage">

  <section class="screen screen--home" aria-label="Home page">
    <header class="app-header">
      <svg class="icon-burger" style="left:18px;top:20px" width="18" height="16" viewBox="0 0 18 16"><rect y="1" width="18" height="3" fill="#5f5f5f"/><rect y="7" width="18" height="3" fill="#5f5f5f"/><rect y="13" width="18" height="3" fill="#5f5f5f"/></svg>
      <div class="brand">Pellora Networks</div>
      <svg class="icon-search" style="left:229px;top:19px" width="20" height="20" viewBox="0 0 20 20"><circle cx="8" cy="8" r="6" fill="none" stroke="#5f5f5f" stroke-width="3"/><line x1="12.5" y1="12.5" x2="18" y2="18" stroke="#5f5f5f" stroke-width="3.5" stroke-linecap="round"/></svg>
    </header>
    <div class="tagline-strip">WEST MICHIGAN'S BEST INTERNET SERVICE</div>
    <div class="hero" role="img" aria-label="Photo of a glowing orange sunset sky">
      <div class="hero__big">4G</div>
      <div class="hero__words">wireless<br>speed</div>
    </div>
    <nav class="tabs">
      <div class="tab tab--active" style="left:0;width:82px">Home<br>Plans</div>
      <div class="tab" style="left:85px;width:80px">Business<br>Plans</div>
      <div class="tab" style="left:168px;width:79px">Optional<br>extras</div>
    </nav>
    <h2 class="section-title">Monthly plans</h2>
    <div class="soft-shadow" style="top:257px"></div>
    <div class="plan">
      <div class="plan__name">Best Value</div>
      <div class="plan__spec">Up to &nbsp;1Mb download</div>
      <div class="plan__spec">Up to 512kbs upload</div>
    </div>
    <div class="price"><span class="price__cur">$</span> <span class="price__main">24</span><span class="price__cents">.99</span></div>
    <div class="slider-arrow slider-arrow--prev"><svg width="33" height="33" viewBox="0 0 33 33"><path d="M19 10 L13 16.5 L19 23" fill="none" stroke="#fff" stroke-width="2.5"/></svg></div>
    <div class="slider-arrow slider-arrow--next"><svg width="33" height="33" viewBox="0 0 33 33"><path d="M14 10 L20 16.5 L14 23" fill="none" stroke="#fff" stroke-width="2.5"/></svg></div>
    <div class="install-fee">+ $100 install fee</div>
    <div class="btn-buy">Buy Now</div>
    <div class="dots"><span class="dot dot--on"></span><span class="dot"></span><span class="dot"></span></div>
    <div class="soft-shadow" style="top:576px"></div>
    <div class="hotline"><svg width="20" height="20" viewBox="0 0 24 24"><path d="M6.6 10.8c1.4 2.8 3.8 5.1 6.6 6.6l2.2-2.2c.3-.3.7-.4 1-.2 1.1.4 2.3.6 3.6.6.6 0 1 .4 1 1V20c0 .6-.4 1-1 1C10.6 21 3 13.4 3 4c0-.6.4-1 1-1h3.5c.6 0 1 .4 1 1 0 1.3.2 2.5.6 3.6.1.3 0 .7-.2 1L6.6 10.8z" fill="#f57b10"/></svg>1-844-7RU-NLOK</div>
  </section>

  <section class="screen screen--menu" aria-label="Navigation menu open">
    <div class="peek" style="left:206px;width:59px">
      <svg style="position:absolute;left:17px;top:22px" width="18" height="16" viewBox="0 0 18 16"><rect y="1" width="18" height="3" fill="#5f5f5f"/><rect y="7" width="18" height="3" fill="#5f5f5f"/><rect y="13" width="18" height="3" fill="#5f5f5f"/></svg>
      <div class="tagline-strip" style="text-align:left;padding-left:17px">WEST MICHIGAN'S</div>
      <div class="hero" role="img" aria-label="Photo of a glowing orange sunset sky"></div>
      <div class="tab tab--active" style="left:28px;top:158px;width:82px;color:#333">Home<br>Plans</div>
    </div>
    <nav class="drawer">
      <div class="drawer__item" style="top:0">Menu item</div>
      <div class="drawer__item" style="top:37px">Menu item</div>
      <div class="drawer__item" style="top:73px">Menu item</div>
      <div class="drawer__item" style="top:109px">Menu item</div>
      <div class="drawer__item drawer__item--open" style="top:146px">Menu item
        <div class="drawer__toggle"><svg style="position:absolute;left:11px;top:12px" width="14" height="12" viewBox="0 0 14 12"><rect width="14" height="2.4" fill="#fff"/><rect y="4.8" width="14" height="2.4" fill="#fff"/><rect y="9.6" width="14" height="2.4" fill="#fff"/></svg></div>
      </div>
      <div class="drawer__item drawer__item--sub" style="top:182px">Menu item</div>
      <div class="drawer__item drawer__item--sub" style="top:218px">Menu item</div>
      <div class="drawer__item drawer__item--current" style="top:255px">Menu item</div>
      <div class="drawer__item" style="top:293px">Menu item</div>
      <div class="drawer__item" style="top:329px">Menu item</div>
      <svg style="position:absolute;left:181px;top:340px" width="17" height="14" viewBox="0 0 17 14"><rect width="17" height="2.6" fill="#6a6a6a"/><rect y="5.7" width="17" height="2.6" fill="#6a6a6a"/><rect y="11.4" width="17" height="2.6" fill="#6a6a6a"/></svg>
      <div class="tap-mark"></div>
    </nav>
  </section>

  <section class="screen screen--search" aria-label="Search panel open">
    <div class="peek" style="left:0;width:59px">
      <svg style="position:absolute;left:24px;top:21px" width="20" height="20" viewBox="0 0 20 20"><circle cx="8" cy="8" r="6" fill="none" stroke="#5f5f5f" stroke-width="3"/><line x1="12.5" y1="12.5" x2="18" y2="18" stroke="#5f5f5f" stroke-width="3.5" stroke-linecap="round"/></svg>
      <div class="tagline-strip" style="text-align:right;width:59px;padding-right:11px">SERVICE</div>
      <div class="hero" style="width:59px" role="img" aria-label="Photo of a glowing orange sunset sky"></div>
      <div class="tab" style="left:-20px;top:158px;width:72px">Optional<br>extras</div>
    </div>
    <aside class="search-panel">
      <div class="search-panel__bar">
        <div class="search-field">
          <div class="search-field__input">Search</div>
          <svg class="search-field__btn" width="20" height="20" viewBox="0 0 20 20"><circle cx="8" cy="8" r="6" fill="none" stroke="#5f5f5f" stroke-width="3"/><line x1="12.5" y1="12.5" x2="18" y2="18" stroke="#5f5f5f" stroke-width="3.5" stroke-linecap="round"/></svg>
        </div>
      </div>
    </aside>
  </section>

</main>
</body>
</html>
```